Chic streamline modern edgy! Danemerecurls.com

I need a website built for my personal business. I am a hair stylist and I would like a crisp website that works well, is sleek, easy to use, and allows my clients to navigate through Services and pay deposits for services listed.

My logo is somewhat of a full moon, so my theme is nocturnal.

My information can be found at chairbook.com/danemerecurls

Target Market(s)

Women ages 25-55 who are looking for luxury hair extension services

Industry/Entity Type

Hair And Beauty

Number of Pages Required

1 page

Colors
474747
919191
d3d3d3
000000

Requirements
Must have
• Location map, coinvale link embedded for deposits, contact box, bio, faq/policies, menu of services, hours of availability by appointment only .
Nice to have
• An interactive calander where I could post dates that I am available, preferred providers for other beauty services where i could list other websites for make up and other beauty related referrals. a bridal tab would be nice to offer information about bridal services and policies.

```html
<!DOCTYPE html>
<html lang="en">
<head>
<meta charset="utf-8">
<title>Danemere Curls — Hair by Dane Mercer</title>
<link href="https://fonts.googleapis.com/css2?family=Ubuntu:wght@300;400;500;700&display=swap" rel="stylesheet">
<style>
:root{
  --ink:#000000;
  --charcoal:#474747;
  --mid:#919191;
  --silver:#d3d3d3;
  --band:#a9a9a9;
  --white:#ffffff;
  --tab:#1e1e24;
  --text:#222222;
}
*{box-sizing:border-box;margin:0;padding:0}
html,body{width:1200px;height:3675px;overflow:hidden}
body{position:relative;font-family:'Ubuntu',sans-serif;color:var(--text);background:var(--white)}
.abs{position:absolute}

/* hero */
.hero{left:0;top:0;width:1200px;height:1033px;background:#e6e6e6;overflow:hidden}
.hero-light{left:83px;top:0;width:1117px;height:680px}
.hero-photo{left:420px;top:0;width:780px;height:1033px;background:linear-gradient(160deg,#d9d9d9 0%,#9a9a9a 35%,#5a5a5a 60%,#8c8c8c 85%,#b5b5b5 100%)}
.side-rail{left:0;top:0;width:83px;height:680px;background:var(--ink)}
.rail-step{left:0;top:680px;width:83px;height:16px;background:var(--mid)}
.rail-foot{left:0;top:960px;width:83px;height:73px;background:var(--charcoal)}
.menu-icon{left:27px;top:32px;width:22px}
.menu-icon span{display:block;height:3px;background:var(--white);margin-bottom:5px}
.brand{left:500px;top:30px;width:200px;text-align:center}
.brand-mark{width:76px;height:76px;border-radius:50%;background:var(--ink);margin:0 auto 10px}
.brand-name{font-weight:300;font-size:23px;letter-spacing:3px;color:#1a1a1a}
.brand-sub{font-weight:300;font-size:13px;letter-spacing:9px;color:#1a1a1a;display:flex;align-items:center;justify-content:center;gap:8px;margin-top:2px}
.brand-sub i{display:block;width:36px;height:1px;background:#1a1a1a}
.tagline{left:133px;top:385px;width:520px}
.tagline h1{font-weight:700;font-size:36px;line-height:40px;letter-spacing:1px;color:var(--ink)}
.tagline h1 small{font-size:30px}
.tagline p{font-size:22px;letter-spacing:1px;color:#333;margin-top:6px;font-weight:400}
.bio{left:83px;top:680px;width:1117px;height:353px;background:rgba(211,211,211,.85)}
.bio p{position:absolute;left:150px;top:62px;width:820px;text-align:center;font-size:13.5px;line-height:26px;letter-spacing:1.1px;color:#222}

.tab{width:172px;height:5px;left:514px;background:var(--tab)}

/* testimonials */
.section-title{width:1200px;left:0;text-align:center;font-weight:500;font-size:27px;letter-spacing:1.5px}
.test-band{left:0;top:1235px;width:1200px;height:345px;background:var(--band)}
.card-img{width:277px;background:linear-gradient(135deg,#c9a48c,#7a4f3a)}
.card-img.b{background:linear-gradient(135deg,#6b4a3c,#3b2620)}
.card-img.c{background:linear-gradient(135deg,#7d6b66,#3e2e2a)}
.card-strip{width:277px;height:82px;top:1490px;opacity:.8}
.arrow{top:1352px;width:38px;height:38px;background:#e8e8e8;display:flex;align-items:center;justify-content:center}
.card-text{top:1615px;width:277px;text-align:center;font-size:10px;line-height:18px;color:#333}
.card-text h3{font-size:12px;font-weight:700;color:#111;padding-bottom:6px;border-bottom:1px solid #bbb;margin-bottom:8px}
.card-text .who{font-weight:500;color:#111}

/* services */
.services{left:0;top:1805px;width:1200px;height:580px;background:var(--ink);color:var(--white)}
.services .section-title{top:45px;color:var(--white)}
.svc-col{top:124px;width:340px}
.svc{font-size:11px;line-height:16.5px;margin-bottom:32px;color:#eee}
.svc h4{font-size:12px;font-weight:700;letter-spacing:.5px}

/* form */
.booking{left:0;top:2385px;width:1200px;height:395px;background:var(--mid)}
.booking .section-title{top:40px;color:var(--white);font-weight:400}
.field{left:460px;width:278px;height:24px;border-bottom:1px solid #c4c4c4;color:var(--white);font-size:14px;letter-spacing:1px;line-height:22px}
.check{display:inline-block;width:9px;height:9px;border:1px solid var(--white);margin:0 10px 0 3px;vertical-align:middle}
.send{left:573px;top:247px;width:54px;height:22px;background:#bdbdbd;color:var(--white);font-size:13px;text-align:center;line-height:22px;letter-spacing:1px}
.pay{left:525px;top:310px;width:150px;text-align:center}
.pay-name{font-size:10px;font-weight:700;color:#2a3f7a;text-align:left;padding-left:2px}
.pay-cards{display:flex;gap:4px;margin-top:2px}
.pay-cards span{width:34px;height:22px;border-radius:2px;background:#d84b2a}
.pay-cards span:nth-child(2){background:#f3f3f3}
.pay-cards span:nth-child(3){background:#2858a8}
.pay-cards span:nth-child(4){background:#3c8ad0}

/* faq */
.faq .section-title{top:2838px}
.faq-list{left:486px;top:2898px;width:500px;font-size:10.5px;line-height:18px;color:#333;list-style:none;letter-spacing:.5px}
.faq-list li{font-weight:500}
.faq-list .answer{font-weight:400;color:#666;padding-left:7px}

/* contact */
.map{left:0;top:3108px;width:570px;height:430px;background:linear-gradient(135deg,#9a9a9a,#7f7f7f 50%,#929292)}
.contact{left:570px;top:3108px;width:630px;height:430px;background:var(--ink);color:var(--white);text-align:center;font-size:10.5px;letter-spacing:.5px;line-height:18px}
.contact h2{font-size:27px;font-weight:500;margin-top:48px;letter-spacing:1px}
.pin{margin:20px auto 14px;display:block}
.hours h5{font-size:12px;font-weight:700;margin-top:34px}

/* social */
.social{left:0;top:3570px;width:1200px;display:flex;justify-content:center;gap:26px}
.social span{width:36px;height:36px;border-radius:50%;background:var(--ink)}
</style>
</head>
<body>

<section class="hero abs">
  <svg class="hero-light abs" viewBox="0 0 1117 680" preserveAspectRatio="none" aria-hidden="true"><polygon points="0,0 520,0 780,680 0,680" fill="#f2f2f2"/><polygon points="0,0 300,0 0,420" fill="#fafafa"/></svg>
  <div class="hero-photo abs" role="img" aria-label="Black and white portrait of the stylist Dane Mercer in a camouflage shirt"></div>
  <div class="side-rail abs"></div>
  <div class="rail-step abs"></div>
  <div class="rail-foot abs"></div>
  <nav class="menu-icon abs" aria-label="Menu"><span></span><span></span><span></span></nav>
  <div class="brand abs">
    <div class="brand-mark"></div>
    <div class="brand-name">DANEMERE CURLS</div>
    <div class="brand-sub"><i></i>HAIR<i></i></div>
  </div>
  <div class="tagline abs">
    <h1>Beautiful hair <small>is every</small><br>woman's perfect ornament!</h1>
    <p>by Dane Mercer</p>
  </div>
  <div class="bio abs">
    <p>Professional Hair Stylist, <b>Dane Mercer</b>, has devolved a signature approach to Hair Design. Dane studied the science of beautiful hair at Larkin Hair Academy in his native city of Dallas Texas. He continues to sharpen his skill set with continued color and cutting education from Orsen Vale, Brandtholm, and Veldara. His love for healthy hair care is emphasized by his ability to create undetectable extensions. These additions not only accentuate his clients appearance, they promote growth and protection of their natural mane. To further his artistic technique, Dane travels to international hair shows and and events in the states and abroad.</p>
  </div>
</section>
<div class="tab abs" style="top:1033px"></div>

<h2 class="section-title abs" style="top:1098px">Testemonials and Clients</h2>
<div class="test-band abs"></div>
<div class="card-img abs" style="left:161px;top:1201px;height:275px" role="img" aria-label="Portrait of a client with long red curls"></div>
<div class="card-img b abs" style="left:461px;top:1194px;height:282px" role="img" aria-label="Bridal makeup close-up with veil"></div>
<div class="card-img c abs" style="left:761px;top:1194px;height:282px" role="img" aria-label="Portrait of a client with long styled hair"></div>
<div class="card-img card-strip abs" style="left:161px"></div>
<div class="card-img b card-strip abs" style="left:461px"></div>
<div class="card-img c card-strip abs" style="left:761px"></div>
<div class="arrow abs" style="left:123px"><svg width="10" height="10" viewBox="0 0 10 10"><path d="M6.5 1 2.5 5l4 4" fill="none" stroke="#333" stroke-width="1.3"/></svg></div>
<div class="arrow abs" style="left:1039px"><svg width="10" height="10" viewBox="0 0 10 10"><path d="M3.5 1l4 4-4 4" fill="none" stroke="#333" stroke-width="1.3"/></svg></div>

<div class="card-text abs" style="left:161px"><h3>Makeup</h3><div class="who">Corinne A. / Dallas</div>"I have been looking for a stylist since I moved to Dallas for 7 years. I noticed a young ladys hair and he gave me Dane information. I LOVE MY HAIR. He does an amazing job. Always leave satisfied!!!"</div>
<div class="card-text abs" style="left:461px"><h3>Brides</h3><div class="who">Mara S. / Dallas</div>"I never leave her shop disappointed! He's miracle worker to say the least :)"</div>
<div class="card-text abs" style="left:761px"><h3>Parties</h3><div class="who">Nadia W. / Dallas</div>"Wonderful hairstylist that will keep your hair healthy and looking great."<br>Thank you!"</div>

<div class="tab abs" style="top:1800px"></div>
<section class="services abs">
  <h2 class="section-title abs">Services and Appointments</h2>
  <div class="svc-col abs" style="left:289px">
    <div class="svc"><h4>// Cleanse/ Style</h4>Thorough shampoo and conditioning services using Meridia hair care products.<br>$55 and up</div>
    <div class="svc"><h4>// Permanent Color</h4>ermanent coloring process which includes shampoo and conditioning services. Consultation is required and relaxed hair will not be permanently colored.<br>$125 and up</div>
    <div class="svc"><h4>// Custom Extensions</h4>ull/Partial Sew In Extensions with cut and style included. Hair must be clean and free of products upon arrival. $25 ...<br>(more)<br>$185 and up</div>
    <div class="svc"><h4>// Extension Removal</h4>Extensions are carefully removed, and hair is thoroughly cleansed and deep conditioned. Trim and style are included.<br>$75 and up</div>
  </div>
  <div class="svc-col abs" style="left:677px">
    <div class="svc"><h4>// Cleanse/ Style</h4>Thorough shampoo and conditioning services using Meridia hair care products.<br>$55 and up</div>
    <div class="svc"><h4>// Permanent Color</h4>ermanent coloring process which includes shampoo and conditioning services. Consultation is required and relaxed hair will not be permanently colored.<br>$125 and up</div>
    <div class="svc"><h4>// Custom Extensions</h4>ull/Partial Sew In Extensions with cut and style included. Hair must be clean and free of products upon arrival. $25 ...<br>(more)<br>$185 and up</div>
    <div class="svc"><h4>// Extension Removal</h4>Extensions are carefully removed, and hair is thoroughly cleansed and deep conditioned. Trim and style are included.<br>$75 and up</div>
  </div>
</section>

<section class="booking abs">
  <h2 class="section-title abs">Drop Me a Line</h2>
  <div class="field abs" style="top:115px">name</div>
  <div class="field abs" style="top:139px">service requested</div>
  <div class="field abs" style="top:163px">/ morning<span class="check"></span>/ afternoon<span class="check"></span>/ evening<span class="check"></span></div>
  <div class="field abs" style="top:187px">e-mail</div>
  <div class="field abs" style="top:211px;height:26px">contact number</div>
  <div class="send abs">send</div>
  <div class="pay abs">
    <div class="pay-name">coinvale</div>
    <div class="pay-cards"><span></span><span></span><span></span><span></span></div>
  </div>
</section>
<div class="tab abs" style="top:2780px"></div>

<section class="faq">
  <h2 class="section-title abs">Faqs / Policies</h2>
  <ul class="faq-list abs">
    <li>+ How do I buy at Danemere Online?</li>
    <li>+ Can I buy online from anywhere in the world?</li>
    <li>+ Do I have to pay Custom Fees and Import Taxes?</li>
    <li>- How can I pay my order?</li>
    <li class="answer">You'll be updated via email at each stage of the transfer. You can<br>also track your transfer with our award winning mobile apps and website wherever you are.</li>
    <li>+ Is it safe to shop at Maison Lune Online?</li>
    <li>+ In which currency do I make the payment?</li>
  </ul>
</section>
<div class="tab abs" style="top:3104px"></div>

<div class="map abs" role="img" aria-label="Greyscale street map of north Dallas with a pin at the salon location"></div>
<section class="contact abs">
  <h2>Contact</h2>
  <svg class="pin" width="24" height="30" viewBox="0 0 24 30" aria-hidden="true"><path d="M12 1C6 1 2 5.5 2 11c0 7 10 18 10 18s10-11 10-18C22 5.5 18 1 12 1z" fill="#fff"/><circle cx="12" cy="11" r="4" fill="#000"/></svg>
  <p>4820 CEDAR ROW,<br>DALLAS, TX 75001</p>
  <p style="margin-top:36px">+00 014 555 72 318<br><span style="display:block;margin-top:5px">CONTACT@DANEMERECURLS.COM</span></p>
  <div class="hours">
    <h5>HOURS</h5>
    <p>TUESDAY &nbsp; 9:00AM - 6:00PM<br>WEDNESDAY &nbsp; 9:00AM - 6:00PM<br>THURSDAY &nbsp; 9:00AM - 6:00PM</p>
  </div>
</section>

<nav class="social abs" aria-label="Social links">
  <span role="img" aria-label="Facet"></span>
  <span role="img" aria-label="Chirpline"></span>
  <span role="img" aria-label="Portfoli"></span>
  <span role="img" aria-label="Linkwork"></span>
  <span role="img" aria-label="Pinboard"></span>
  <span role="img" aria-label="Journalry"></span>
</nav>

</body>
</html>
```